Re-drawing and gpahically, according to coorporate design

Three flowcharts need to be re-drawn and graphically improved according to coorporate design

```html
<!DOCTYPE html>
<html lang="en">
<head>
<meta charset="utf-8">
<title>Flowchart 01 – Biomass, Residues and CO₂ Pathways</title>
<link rel="stylesheet" href="https://fonts.googleapis.com/css2?family=Open+Sans:wght@400;700&display=swap">
<style>
  :root {
    --forest: #347f3a;
    --forest-halo: #a9c9a4;
    --slate: #476664;
    --slate-halo: #c6cfce;
    --graphite: #6d6a6a;
    --graphite-halo: #c8c5c5;
    --sage: #a3c3be;
    --sage-halo: #d8e6e3;
    --olive: #97a608;
    --olive-halo: #d5dc9c;
    --mist: #d2dad9;
    --mist-halo: #eceeee;
    --sun: #ffc400;
    --ink: #2b2b2b;
    --paper: #ffffff;
    --pattern: #eef2d6;
  }
  html, body {
    margin: 0;
    padding: 0;
    width: 908px;
    height: 1200px;
    overflow: hidden;
    background: var(--paper);
  }
  .canvas { display: block; width: 908px; height: 1200px; }
  text { font-family: "Open Sans", sans-serif; }
  .title { font-size: 34px; font-weight: 400; fill: var(--ink); letter-spacing: 1px; }
  .label { font-size: 20px; font-weight: 700; fill: #fff; text-anchor: middle; letter-spacing: .5px; }
  .label-dark { font-size: 20px; font-weight: 700; fill: var(--ink); text-anchor: middle; }
  .label-light { font-size: 20px; font-weight: 400; fill: var(--ink); text-anchor: middle; letter-spacing: .3px; }
  .formula { font-size: 30px; font-weight: 700; fill: var(--ink); text-anchor: middle; }
  .formula-white { font-size: 34px; font-weight: 700; fill: #fff; text-anchor: middle; }
  .tag { font-size: 15px; font-weight: 700; fill: var(--ink); text-anchor: middle; }
  .footnote { font-size: 15px; fill: #111; text-anchor: middle; }
  .flow { fill: none; stroke-width: 6; stroke-linejoin: miter; }
  .flow-forest { stroke: var(--forest); marker-end: url(#head-forest); }
  .flow-slate { stroke: var(--slate); marker-end: url(#head-slate); }
  .flow-graphite { stroke: var(--graphite); marker-end: url(#head-graphite); }
  .flow-sage { stroke: var(--sage); marker-end: url(#head-sage); }
  .flow-olive { stroke: var(--olive); marker-end: url(#head-olive); }
  .flow-sun { stroke: var(--sun); marker-end: url(#head-sun); }
  .node { stroke-width: 10; stroke-linejoin: round; }
  .forest { fill: var(--forest); stroke: var(--forest-halo); }
  .slate { fill: var(--slate); stroke: var(--slate-halo); }
  .graphite { fill: var(--graphite); stroke: var(--graphite-halo); }
  .sage { fill: var(--sage); stroke: var(--sage-halo); }
  .olive { fill: var(--olive); stroke: var(--olive-halo); }
  .mist { fill: var(--mist); stroke: var(--mist-halo); }
  .sun-disc, .sun-ray { fill: var(--sun); }
</style>
</head>
<body>
<svg class="canvas" viewBox="0 0 1600 2115" preserveAspectRatio="none" xmlns="http://www.w3.org/2000/svg">
  <defs>
    <marker id="head-forest" viewBox="0 0 10 10" refX="9" refY="5" markerWidth="4" markerHeight="4" orient="auto"><path d="M0 0L10 5L0 10z" fill="#347f3a"/></marker>
    <marker id="head-slate" viewBox="0 0 10 10" refX="9" refY="5" markerWidth="4" markerHeight="4" orient="auto"><path d="M0 0L10 5L0 10z" fill="#476664"/></marker>
    <marker id="head-graphite" viewBox="0 0 10 10" refX="9" refY="5" markerWidth="4" markerHeight="4" orient="auto"><path d="M0 0L10 5L0 10z" fill="#6d6a6a"/></marker>
    <marker id="head-sage" viewBox="0 0 10 10" refX="9" refY="5" markerWidth="4" markerHeight="4" orient="auto"><path d="M0 0L10 5L0 10z" fill="#a3c3be"/></marker>
    <marker id="head-olive" viewBox="0 0 10 10" refX="9" refY="5" markerWidth="4" markerHeight="4" orient="auto"><path d="M0 0L10 5L0 10z" fill="#97a608"/></marker>
    <marker id="head-sun" viewBox="0 0 10 10" refX="9" refY="5" markerWidth="4" markerHeight="4" orient="auto"><path d="M0 0L10 5L0 10z" fill="#ffc400"/></marker>
    <radialGradient id="pattern-wash" cx="50%" cy="48%" r="60%">
      <stop offset="0" stop-color="#eef2d6"/>
      <stop offset="0.6" stop-color="#eef2d6" stop-opacity=".85"/>
      <stop offset="1" stop-color="#eef2d6" stop-opacity="0"/>
    </radialGradient>
    <polygon id="ray-long" points="-11,-68 0,-134 11,-68"/>
    <polygon id="ray-short" points="-10,-66 0,-124 10,-66"/>
  </defs>

  <!-- background decoration -->
  <rect class="backdrop" x="0" y="300" width="1600" height="1500" fill="url(#pattern-wash)" role="img" aria-label="Faint molecule pattern in pale green"/>

  <text class="title" x="1210" y="74" text-anchor="middle">FLOWCHART - 01</text>

  <!-- sun -->
  <g class="sun" transform="translate(211 210)" role="img" aria-label="Sun">
    <use class="sun-ray" href="#ray-long"/>
    <use class="sun-ray" href="#ray-short" transform="rotate(30)"/>
    <use class="sun-ray" href="#ray-short" transform="rotate(60)"/>
    <use class="sun-ray" href="#ray-long" transform="rotate(90)"/>
    <use class="sun-ray" href="#ray-short" transform="rotate(120)"/>
    <use class="sun-ray" href="#ray-short" transform="rotate(150)"/>
    <use class="sun-ray" href="#ray-long" transform="rotate(180)"/>
    <use class="sun-ray" href="#ray-short" transform="rotate(210)"/>
    <use class="sun-ray" href="#ray-short" transform="rotate(240)"/>
    <use class="sun-ray" href="#ray-long" transform="rotate(270)"/>
    <use class="sun-ray" href="#ray-short" transform="rotate(300)"/>
    <use class="sun-ray" href="#ray-short" transform="rotate(330)"/>
    <circle class="sun-disc" r="58"/>
  </g>

  <!-- connectors -->
  <g class="connectors">
    <path class="flow flow-sun" d="M352 190H462M352 224H462M352 258H462"/>
    <path class="flow flow-sun" d="M155 348V458M189 348V458M223 348V458"/>
    <path class="flow flow-forest" d="M647 220H812"/>
    <path class="flow flow-slate" d="M997 220H1345"/>
    <path class="flow flow-slate" d="M997 248H1175V423H1345"/>
    <path class="flow flow-slate" d="M905 303V458"/>
    <path class="flow flow-forest" d="M553 303V540H820"/>
    <path class="flow flow-graphite" d="M189 623V765"/>
    <path class="flow flow-sage" d="M189 962V1105"/>
    <path class="flow flow-sage" d="M189 1273V1527"/>
    <path class="flow flow-forest" d="M881 620V673H673V765"/>
    <path class="flow flow-forest" d="M905 620V765"/>
    <path class="flow flow-forest" d="M929 620V673H1135V765"/>
    <path class="flow flow-forest" d="M585 865H515"/>
    <path class="flow flow-forest" d="M1222 838H1273V686H1345"/>
    <path class="flow flow-forest" d="M1222 865H1345"/>
    <path class="flow flow-forest" d="M1222 891H1273V1045H1345"/>
    <path class="flow flow-forest" d="M905 962V1105"/>
    <path class="flow flow-slate" d="M845 1250V1320H447V1432"/>
    <path class="flow flow-slate" d="M870 1262V1367H673V1432"/>
    <path class="flow flow-slate" d="M905 1270V1432"/>
    <path class="flow flow-slate" d="M937 1262V1362H1135V1432"/>
    <path class="flow flow-slate" d="M966 1250V1320H1432V1432"/>
    <path class="flow flow-sage" d="M447 1625V1720M673 1625V1720M905 1625V1720M1135 1625V1720"/>
    <path class="flow flow-olive" d="M1432 1625V1720"/>
  </g>

  <!-- top row -->
  <rect class="node forest" x="462" y="145" width="185" height="158" rx="22"/>
  <text class="label" x="555" y="217">AGRICULTURE/<tspan x="555" dy="24">FORESTRY</tspan></text>
  <rect class="node slate" x="812" y="145" width="185" height="158" rx="22"/>
  <text class="label" x="905" y="225">INDUSTRY</text>
  <circle class="node forest" cx="1430" cy="222" r="83"/>
  <text class="label" x="1430" y="229">FOOD/FEED</text>
  <circle class="node mist" cx="1430" cy="423" r="83"/>
  <text class="label-dark" x="1430" y="404">WOOD<tspan x="1430" dy="24">BASED</tspan><tspan x="1430" dy="24">PRODUCTS</tspan></text>

  <circle class="node graphite" cx="189" cy="540" r="83"/>
  <text class="label" x="189" y="536">RENEWABLE<tspan x="189" dy="24">ELECTRICITY</tspan></text>
  <circle class="node forest" cx="905" cy="540" r="83"/>
  <text class="label" x="905" y="547">RESIDUES</text>

  <!-- process row -->
  <polygon class="node sage" points="189,770 277,818 277,912 189,960 101,912 101,818"/>
  <text class="label-dark" x="189" y="872">ELECTROLYSIS</text>

  <rect class="tag-pill" x="343" y="730" width="178" height="35" rx="17" fill="#d5dada"/>
  <text class="tag" x="432" y="753">GREETING THE GAS</text>
  <circle class="node mist" cx="432" cy="865" r="83"/>
  <text class="formula" x="428" y="875">CH<tspan font-size="17" dy="8">4</tspan></text>

  <polygon class="node olive" points="673,770 761,818 761,912 673,960 585,912 585,818"/>
  <text class="label" x="671" y="860">ANAEROBIC<tspan x="671" dy="24">DIGESTION</tspan></text>
  <polygon class="node olive" points="905,770 993,818 993,912 905,960 817,912 817,818"/>
  <text class="label" x="901" y="860">BIOMASS<tspan x="901" dy="24">GASIFICATION</tspan></text>
  <polygon class="node olive" points="1135,770 1223,818 1223,912 1135,960 1047,912 1047,818"/>
  <text class="label" x="1138" y="871">FERMENTATION</text>

  <circle class="node olive" cx="1430" cy="680" r="83"/>
  <text class="label" x="1430" y="687">POLYMERS</text>
  <circle class="node olive" cx="1430" cy="865" r="83"/>
  <text class="label" x="1430" y="872">CHEMICALS</text>
  <circle class="node olive" cx="1430" cy="1045" r="83"/>
  <text class="label" x="1430" y="1052">FUELS</text>

  <circle class="node sage" cx="189" cy="1190" r="83"/>
  <text class="formula" x="186" y="1199">H<tspan font-size="17" dy="8">2</tspan></text>
  <circle class="node slate" cx="905" cy="1190" r="83"/>
  <text class="formula-white" x="900" y="1198">CO<tspan font-size="19" dy="10">2</tspan></text>

  <polygon class="node graphite" points="189,1530 316,1600 316,1740 189,1810 62,1740 62,1600"/>
  <text class="label" x="184" y="1630">VARIOUS DIRECT<tspan x="186" dy="24.5">APPLICATIONS</tspan><tspan x="186" dy="24.5">-MOBILITY</tspan><tspan x="186" dy="24.5">-INDUSTRY</tspan><tspan x="186" dy="24.5">-GAS GRID</tspan></text>

  <!-- CO2 conversion row -->
  <polygon class="node sage" points="447,1435 535,1483 535,1577 447,1625 359,1577 359,1483"/>
  <text class="label-light" x="447" y="1511">CATALYTIC/<tspan x="447" dy="24.5">BIOLOGICAL</tspan><tspan x="447" dy="24.5">METHANATION</tspan></text>
  <polygon class="node sage" points="673,1435 761,1483 761,1577 673,1625 585,1577 585,1483"/>
  <text class="label-light" x="673" y="1511">ELECTRO-<tspan x="673" dy="24.5">CHEMICAL</tspan><tspan x="673" dy="24.5">CONVERSION</tspan></text>
  <polygon class="node sage" points="905,1435 993,1483 993,1577 905,1625 817,1577 817,1483"/>
  <text class="label-light" x="903" y="1503">OTHER<tspan x="903" dy="24.5">CHEMICAL</tspan><tspan x="905" dy="24.5">TRANSFOR-</tspan><tspan x="905" dy="24.5">MATIONS</tspan></text>
  <polygon class="node sage" points="1135,1435 1223,1483 1223,1577 1135,1625 1047,1577 1047,1483"/>
  <text class="label-light" x="1135" y="1515">EXISTING<tspan x="1135" dy="24.5">INDUSTRIAL</tspan><tspan x="1137" dy="24.5">APPLICATIONS</tspan></text>
  <polygon class="node olive" points="1430,1435 1518,1483 1518,1577 1430,1625 1342,1577 1342,1483"/>
  <text class="label" x="1428" y="1540">ALGEA</text>

  <!-- products row -->
  <circle class="node sage" cx="449" cy="1805" r="83"/>
  <text class="formula" x="445" y="1811">CH<tspan font-size="17" dy="8">4</tspan></text>
  <circle class="node sage" cx="675" cy="1805" r="83"/>
  <text class="label-light" x="675" y="1773">E.G.<tspan x="677" dy="24.5">ETHYLENE-</tspan><tspan x="677" dy="24.5">OXIDE</tspan><tspan x="677" dy="24.5">C<tspan font-size="13" dy="5">2</tspan><tspan dy="-5">H</tspan><tspan font-size="13" dy="5">4</tspan><tspan dy="-5">O</tspan></tspan></text>
  <circle class="node sage" cx="906" cy="1805" r="83"/>
  <text class="label-light" x="906" y="1775">E.G.<tspan x="906" dy="24.5">POLYOLS,</tspan><tspan x="906" dy="24.5">POLYMERS,</tspan><tspan x="908" dy="24.5">ETC.</tspan></text>
  <circle class="node sage" cx="1136" cy="1805" r="83"/>
  <text class="label-light" x="1136" y="1786">E.G.<tspan x="1136" dy="24.5">BEVERAGE</tspan><tspan x="1138" dy="24.5">INDUSTRY</tspan></text>
  <circle class="node olive" cx="1432" cy="1805" r="83"/>
  <text class="label" x="1430" y="1797">FUEL,<tspan x="1432" dy="24.5">BIOPOLYMERS</tspan></text>

  <!-- footnote -->
  <text class="footnote" x="800" y="2009">Lorem ipsum dolor sit amet, consectetuer adipiscing elit, sed diam nonummy nibh euismod tincidunt ut laoreet dolore magna aliquam erat volutpat. Ut wisi enim ad minim veniam, quis</text>
  <text class="footnote" x="800" y="2026">nostrud exerci tation ullamcorper suscipit lobortis nisl ut aliquip ex ea</text>
  <text class="footnote" x="800" y="2043">commodo consequat. Duis autem vel eum iriure dolor in hendrerit in vulputate velit esse molestie consequat,</text>
  <text class="footnote" x="800" y="2061">vel illum dolore eu feugiat nulla fac</text>
</svg>
</body>
</html>
```